New Hotel Showcase Website

We plan to launch a website called www.brindlestays.net which showcases the world’s best new hotels. We want a mock up for 2 pages: the homepage (page 1) and the individual hotel page (page 2). We are looking for a design which combines simplicity while highlighting images/features of the hotel. Because the theme of the site is new hotels it is important that the design somehow emphasizes the age of each hotel listed – both on the homepage and then on the individual hotel page.

NOTE: WE WANT A CREATIVE, NEW APPROACH TO DISPLAYING HOTELS. NOT JUST A COPY OF CURRENT HOTEL WEBSITES.

The design should consider unique and creative ways of helping users to navigate the homepage (page 1) based on the age, location or style of the hotel they are interested in. The individual hotel page(page 2) can be more standard by clearly setting out hotel photos, feature lists, reviews, contact details and potential discounts. There is no booking system needed as this is not a hotel booking website.

The design should ideally be compatible with a content management system such as Page Loom. In terms of reference materials we like sites similar to:

http://www.velmarquay.net
http://www.corvidandpine.net
http://www.tessarooms.net
http://www.quillbeds.net

These sites are designed far more simply than large booking sites such as www.roamvix.net, www.bunkfold.net or even wander ledger. However, we are not looking for a copy of the above. We are looking for a design that presents hotels in a novel way and would be seen by the industry as a unique way of displaying new hotels.
Updates

Dear Designers - we have received quite a few entries already. Thank you. However, none of the designs submitted have responded to our brief. They are all copies or derivatives of current hotel websites which is not what we are looking for. We want (a) a new and creative approach to a hotel website and (b) one which creatively uses the age of the hotel (ie. 1 month old, 6 months old etc).

It will require creative thinking and new ideas. We wanted to challenge designers to come up with something new. Thanks.

```html
<!DOCTYPE html>
<html lang="en">
<head>
<meta charset="utf-8">
<title>Brindle Stays — New Hotels</title>
<link rel="stylesheet" href="https://fonts.googleapis.com/css2?family=PT+Sans:wght@400;700&family=Roboto+Condensed:wght@300;400&family=Tinos&family=Open+Sans:wght@400&display=swap">
<style>
:root{
  --blue:#0fa0dc;
  --blue-dark:#0a86bd;
  --ink:#2a2a2a;
  --text:#4a4a4a;
  --page:#f0f0f0;
  --bar:#2c2e30;
  --footer:#2a2b2d;
  --footer-base:#1c1d1f;
  --footer-text:#b8b8b8;
  --tab-dark:#7a7a7a;
  --tab-light:#bdbdbd;
  --tab-darker:#555;
}
*{box-sizing:border-box;margin:0;padding:0}
html,body{width:1200px;height:1198px;overflow:hidden}
body{background:var(--page);font-family:"PT Sans",sans-serif;color:var(--text);position:relative}
.abs{position:absolute}

/* header */
.site-header{position:absolute;left:0;top:0;width:1200px;height:116px;background:#fff}
.brand{position:absolute;left:126px;top:36px;display:flex;align-items:center;gap:10px;font-family:"PT Sans",sans-serif;font-size:30px;font-weight:400;color:var(--blue)}
.brand-dot{width:16px;height:16px;border-radius:50%;background:var(--blue)}
.main-nav{position:absolute;right:128px;top:73px;display:flex;gap:17px;font-family:"Tinos",serif;font-size:14px;color:#111}
.main-nav .active{color:var(--blue)}

/* search bar */
.search-bar{position:absolute;left:0;top:116px;width:1200px;height:39px;background:var(--bar);color:#fff}
.search-bar .label{position:absolute;left:155px;top:9px;font-size:17px}
.radio{position:absolute;top:13px;display:flex;align-items:center;gap:5px;font-size:13px}
.radio i{width:13px;height:13px;border-radius:50%;background:#fff;display:block;position:relative}
.radio.on i::after{content:"";position:absolute;left:3px;top:3px;width:7px;height:7px;border-radius:50%;background:var(--blue)}
.select{position:absolute;top:8px;height:23px;background:#fff;color:#222;font-size:13px;padding:4px 8px}
.select svg{position:absolute;right:9px;top:8px}
.search-btn{position:absolute;left:955px;top:9px;width:74px;height:22px;background:var(--blue);border:1px solid #59c3ef;font-family:"Tinos",serif;font-size:12px;color:#fff;text-align:center;line-height:20px}

/* age tabs */
.age-tabs{position:absolute;left:126px;top:155px;width:948px;height:40px;display:flex}
.age-tabs li{list-style:none;flex:1;text-align:center;font-family:"Roboto Condensed",sans-serif;font-size:13px;color:#555;padding-top:11px;border-bottom:4px solid var(--tab-light)}
.age-tabs li.d{border-bottom-color:var(--tab-dark)}
.age-tabs li.dd{border-bottom-color:var(--tab-darker)}

.section-title{position:absolute;font-family:"Roboto Condensed",sans-serif;font-weight:300;font-size:23px;color:#444}

/* featured */
.featured{position:absolute;left:126px;top:245px;width:640px;height:372px;background:linear-gradient(135deg,#3a3530 0%,#2a2622 45%,#1d1b19 100%);color:#fff}
.featured .name{position:absolute;left:55px;top:102px;display:flex;align-items:baseline;gap:10px;font-size:21px;color:var(--blue)}
.featured .new{font-size:17px;color:#ddd}
.featured .new small{font-size:13px}
.featured .desc{position:absolute;left:55px;top:136px;width:270px;font-size:12px;line-height:16px;color:#e6e6e6}
.meta{position:absolute;top:218px;display:flex;gap:8px;font-size:11.5px;line-height:13px}
.meta span{display:block;color:#888}
.map-box{position:absolute;left:387px;top:91px;width:205px;height:140px;background:#e9e4da;border-radius:3px}
.details-btn{position:absolute;left:446px;top:240px;width:76px;height:25px;background:var(--blue);border:1px solid #6acbf2;font-family:"Tinos",serif;font-size:13px;color:#111;text-align:center;line-height:23px}

/* recently added */
.recent{position:absolute;left:771px;top:245px;width:303px;height:372px;background:linear-gradient(160deg,#5e1d20 0%,#8a2a2c 40%,#b8b3ad 75%,#6c6864 100%)}
.age-badge{position:absolute;right:0;top:0;width:105px;height:30px;background:var(--blue);color:#111;font-size:15px;display:flex;align-items:center;justify-content:center;gap:7px}
.recent .overlay{position:absolute;left:0;bottom:0;width:100%;height:126px;background:rgba(20,20,20,.85);color:#fff;padding:16px 22px}
.recent h3{font-weight:400;font-size:20px}
.recent p{font-size:11.5px;line-height:15px;margin-top:4px;color:#e0e0e0}
.recent .links{display:flex;gap:16px;margin-top:12px;font-size:17px;align-items:center}
.recent .links span{display:flex;align-items:center;gap:9px}

/* welcome */
.welcome-title,.newest-title{position:absolute;top:654px;font-family:"Roboto Condensed",sans-serif;font-weight:300;font-size:24px;color:var(--blue)}
.lead{position:absolute;left:126px;top:692px;width:610px;font-family:"Roboto Condensed",sans-serif;font-size:15.5px;line-height:17px;color:#222}
.body-copy{position:absolute;left:126px;top:743px;width:610px;font-family:"Open Sans",sans-serif;font-size:11.3px;line-height:17.2px;color:#444}
.read-more{position:absolute;left:125px;top:848px;width:81px;height:25px;background:var(--blue);color:#fff;font-family:"Roboto Condensed",sans-serif;font-size:15px;text-align:center;line-height:25px}
.newest-list{position:absolute;left:775px;top:694px;width:299px;list-style:none}
.newest-list li{height:29px;border-bottom:1px dashed #c8c8c8;background:#e6e6e6;color:var(--blue);font-size:14px;padding:5px 11px}
.newest-list li.active{background:var(--blue);color:#fff;border-bottom:none;border-top:1px dashed #8bd3f2}

/* footer */
.site-footer{position:absolute;left:0;top:931px;width:1200px;height:221px;background:var(--footer)}
.foot-title{position:absolute;top:32px;font-family:"Tinos",serif;font-size:14px;color:var(--blue);letter-spacing:.3px}
.foot-list{position:absolute;top:62px;list-style:none;font-family:"Open Sans",sans-serif;font-size:10px;line-height:15.8px;color:var(--footer-text)}
.foot-about{position:absolute;left:762px;top:62px;width:290px;font-family:"Open Sans",sans-serif;font-size:11.3px;line-height:15.8px;color:#ddd}
.foot-base{position:absolute;left:0;top:1152px;width:1200px;height:46px;background:var(--footer-base);text-align:center;font-family:"Open Sans",sans-serif;font-size:11px;color:#999;line-height:46px}
</style>
</head>
<body>

<header class="site-header">
  <div class="brand"><span class="brand-dot"></span>brindlestays.net</div>
  <nav class="main-nav">
    <span class="active">HOME</span><span>ABOUT US</span><span>HOTELS</span><span>CONTACT US</span>
  </nav>
</header>

<section class="search-bar">
  <span class="label">Search Hotels :</span>
  <span class="radio" style="left:275px"><i></i>All</span>
  <span class="radio on" style="left:317px"><i></i>Custom Search</span>
  <div class="select" style="left:433px;width:166px">Location<svg width="12" height="7" viewBox="0 0 12 7"><path d="M1 1l5 5 5-5" fill="none" stroke="#555"/></svg></div>
  <div class="select" style="left:607px;width:166px">Age<svg width="12" height="7" viewBox="0 0 12 7"><path d="M1 1l5 5 5-5" fill="none" stroke="#555"/></svg></div>
  <div class="select" style="left:782px;width:165px">Style<svg width="12" height="7" viewBox="0 0 12 7"><path d="M1 1l5 5 5-5" fill="none" stroke="#555"/></svg></div>
  <div class="search-btn">SEARCH</div>
</section>

<ul class="age-tabs">
  <li class="d">1 months</li><li>1-3 months</li><li class="d">3-6 months</li><li>1 year</li><li class="d">3 years</li><li>3-6 years</li><li class="d">6-10 years</li><li>15 years</li><li class="dd">30 years</li><li>Older</li>
</ul>

<h2 class="section-title" style="left:125px;top:208px">Featured Hotels</h2>
<h2 class="section-title" style="left:770px;top:208px">Recently Added</h2>

<article class="featured" role="img" aria-label="Dim hotel suite interior with sofa, window plants and fruit bowl">
  <div class="name">Hotel Name
    <svg width="20" height="19" viewBox="0 0 24 23"><polygon points="12,1 15,8.5 23,9 17,14.5 19,22 12,18 5,22 7,14.5 1,9 9,8.5" fill="#f5b82a"/></svg>
    <span class="new">NEW <small>[ 1 month ]</small></span>
  </div>
  <p class="desc">Lorem ipsum dolor sit amet, consectetur adipiscing elit. Sed id tempus enim. Etiam eros velit, rutrum in fringilla id, fermentum sit amet nulla. Nullam cursus ut lorem commodo eu pharetra elit blandit.</p>
  <div class="meta" style="left:56px"><svg width="12" height="17" viewBox="0 0 12 17"><path d="M6 0a6 6 0 0 0-6 6c0 4 6 11 6 11s6-7 6-11a6 6 0 0 0-6-6z" fill="#fff"/><circle cx="6" cy="6" r="2.3" fill="#2a2622"/></svg><div>Location<span>New York</span></div></div>
  <div class="meta" style="left:156px"><svg width="12" height="16" viewBox="0 0 12 16"><path d="M1 1h10M1 15h10M2 1c0 5 8 5 8 7s-8 2-8 7M10 1c0 5-8 5-8 7s8 2 8 7" fill="none" stroke="#fff" stroke-width="1.3"/></svg><div>Age<span>1 month</span></div></div>
  <div class="meta" style="left:233px"><svg width="12" height="16" viewBox="0 0 12 16"><path d="M1 1h10L6 7zM6 7v8M3 15h6" fill="none" stroke="#fff" stroke-width="1.3"/></svg><div>Style<span>Lorem ipsum</span></div></div>
  <div class="map-box" role="img" aria-label="Street map showing the hotel location"></div>
  <div class="details-btn">DETAILS</div>
</article>

<article class="recent" role="img" aria-label="Restaurant table with wine glasses and red drapes">
  <div class="age-badge"><svg width="18" height="17" viewBox="0 0 24 23"><polygon points="12,1 15,8.5 23,9 17,14.5 19,22 12,18 5,22 7,14.5 1,9 9,8.5" fill="#f5b82a"/></svg>1 Months</div>
  <div class="overlay">
    <h3>Hotel Name</h3>
    <p>Lorem ipsum dolor sit amet, consectetur adipiscing elit. id tempus enim. Etiam eros velit,</p>
    <div class="links">
      <span><svg width="25" height="25" viewBox="0 0 25 25"><circle cx="12.5" cy="12.5" r="12.5" fill="#0fa0dc"/><path d="M12.5 5a4.5 4.5 0 0 0-4.5 4.5c0 3.3 4.5 9.5 4.5 9.5s4.5-6.2 4.5-9.5A4.5 4.5 0 0 0 12.5 5z" fill="#111"/><circle cx="12.5" cy="9.5" r="1.7" fill="#0fa0dc"/></svg>Map</span>
      <span><svg width="25" height="25" viewBox="0 0 25 25"><circle cx="12.5" cy="12.5" r="12.5" fill="#0fa0dc"/><rect x="7" y="8" width="11" height="9" fill="none" stroke="#111" stroke-width="1.5"/><path d="M8 16l3-4 2 2 2-3 2 5z" fill="#111"/></svg>Image</span>
    </div>
  </div>
</article>

<h2 class="welcome-title" style="left:125px">Welcome to Brindle Stays</h2>
<p class="lead">Lorem ipsum dolor sit amet, consectetur adipiscing elit. Sed id tempus enim. Etiam eros velit, rutrum in fringilla id, fermentum sit amet nulla. Nullam cursus mi ut lorem commodo eu pharetra elit blandit.</p>
<p class="body-copy">Aenean dapibus lorem laoreet ante pharetra ornare malesuada orci ornare. Ut volutpat ipsum ipsum, eget suscipit mauris. Sed sed nisl ac justo rutrum convallis. Fusce facilisis, nunc et viverra iaculis, arcu augue tempor ipsum, ut auctor sapien justo ac metus. Morbi adipiscing sodales condimentum. Nunc porta hendrerit turpis, nec pharetra enim interdum id. Donec vel metus adipiscing tortor facilisis venenatis. Mauris vel volutpat leo. Nunc non justo nunc. Donec sapien arcu, egestas at facilisis et, interdum eget mauris.</p>
<div class="read-more">Read More</div>

<h2 class="newest-title" style="left:774px">Newest Hotels</h2>
<ul class="newest-list">
  <li class="active">1 Month</li><li>3 Months</li><li>6 Months</li><li>12 Months</li><li>15 Months</li><li>18 Months</li>
</ul>

<footer class="site-footer">
  <h4 class="foot-title" style="left:148px">HOTELS BY LOCATION</h4>
  <ul class="foot-list" style="left:149px"><li>Abu Dhabi</li><li>Auckland</li><li>Bangkok</li><li>Cape Town</li><li>Dubai</li><li>Florida</li><li>Goa</li><li>Hongkong</li></ul>
  <ul class="foot-list" style="left:269px"><li>Istanbul</li><li>Lisbon</li><li>London</li><li>Madrid</li><li>Manchester</li><li>Milan</li><li>Moscow</li><li>New york</li></ul>
  <ul class="foot-list" style="left:397px"><li>Paris</li><li>Rio de Janeiro</li><li>Singapore</li><li>Sydney</li><li>Thailand</li><li>Tokyo</li><li>Venis</li><li>Zurich</li></ul>
  <h4 class="foot-title" style="left:545px">HOTELS BY AGE</h4>
  <ul class="foot-list" style="left:546px"><li>1 year</li><li>1-5 years</li><li>5-10 years</li><li>10-15 years</li><li>15-30 years</li><li>30-60 years</li><li>60-100 years</li><li>More than 100 years</li></ul>
  <h4 class="foot-title" style="left:761px">ABOUT BRINDLESTAYS.NET</h4>
  <p class="foot-about">Lorem ipsum dolor sit amet, consectetur adipiscing elit. Sed id tempus enim. Etiam eros velit, rutrum in fringilla id, fermentum sit amet nulla. Nullam cursus mi ut lorem commodo eu pharetra elit blandit. Phasellus malesuada, massa et adipiscing tempor, tellus lacus vulputate dui, non commodo mi neque a dui. Praesent enim dolor,</p>
</footer>
<div class="foot-base">© Copyright 2013. All Rights Reserved</div>

</body>
</html>
```